Gum Care Season infographic - Bright Grins for Every Year

To create an infographic for Gum Care Season, August 2014, with the key messages of how the health of your mouth affects you through your lifetime.
We require two posters (A3 and A4 options) that will educate the Australian and New Zealand public of the importance of maintaining good oral health through facts and statistics (see attachments), focusing on different stages in your life.
The A3 poster will be used for: hanging in dental practices, posted in social media, on websites, advertising, public relations.
The A4 poster will be used for print handouts, websites, advertising, public relations.
Sections of the posters will be pulled out to be used in social media posts, on websites, in emails, etc.
Design constraints:
Poster One: Infographic Poster to be A3 (Appendix 1)
Poster Two: Infographic Poster to be reconfigured as A4 handout with limited facts (Appendix 2).
Full colour with the PVR colour palette reflected throughout.
Deliverables:
Design two infographics to reflect the tagline, Bright Grins for Every Year, and:
• One A3 poster to represents the key milestones as outlined in Appendix 1.
One A4 poster/handout to represent the key milestones in Appendix 2.
• Is obvious that these are stages in your life but does not mention the specific ages.
• Facts can be represented in icons, images, graphs, fractions, percentages, etc.
• Can be broken into smaller campaign sub messages.
• Includes: Gum Care Season and Bright Grins for Every Year text.
• Includes: A PVR Initiative logo.
• Includes August 2014 as Gum Care Season.
• Include website: www.pivoradental.example
• Is similar in style to the PVR launch infographic (attached).
• Clean, vibrant, understandable and friendly.
Tone:
PVR is experienced, reliable, caring, accessible, knowledgeable, friendly and confident in all aspects of dentistry.
The infographic can be ‘Tongue in cheek’ – friendly tone to suit different age groups through the messages, ie. 18-25 years is more conversational and cheeky, while 50+ could come from a ‘dad joke.’
See attached logo, colour palette and appendices.
Target Market(s)
Aussie and Kiwi families visiting a modern, bright, well-presented dental practice.
Industry/Entity Type
Health
Requirements
Must have
- Bright, clear and engaging. Needs to be suited to a professional dental practice, but also stand out on social media and in advertising.
Must have name of campaign and month, brand supporter, website - see brief.

```html
<!DOCTYPE html>
<html lang="en">
<head>
<meta charset="utf-8">
<title>Gum Care Season – Bright Grins for Every Year</title>
<link rel="stylesheet" href="https://fonts.googleapis.com/css2?family=Oswald:wght@400;500;700&family=Roboto+Condensed:wght@400;700&display=swap">
<style>
  :root {
    --sky: #2b9ad8;
    --sky-deep: #2388c4;
    --navy: #17335b;
    --sun: #f8c227;
    --white: #ffffff;
  }
  * { margin: 0; padding: 0; box-sizing: border-box; }
  html, body { width: 849px; height: 1200px; overflow: hidden; background: var(--sky); }
  .poster {
    position: relative; width: 849px; height: 1200px; overflow: hidden;
    background: radial-gradient(circle at 50% 40%, var(--sky) 0%, var(--sky-deep) 100%);
    color: var(--white); font-family: "Roboto Condensed", "Arial Narrow", sans-serif;
  }
  .topline {
    position: absolute; top: 26px; left: 0; width: 100%; text-align: center;
    font-family: "Oswald", sans-serif; font-size: 22px; letter-spacing: 1px; font-weight: 500;
  }
  .topline .brand { font-weight: 700; font-size: 26px; margin: 0 6px; }
  .topline .sep { margin: 0 14px; opacity: .8; }

  .title-block { position: absolute; left: 34px; top: 170px; width: 540px; height: 150px; }
  .title-month {
    position: absolute; left: 0; top: 0; width: 250px; height: 130px; background: var(--navy);
    font-family: "Oswald", sans-serif; font-weight: 700; line-height: 1; padding: 14px 18px;
    transform: rotate(-3deg);
  }
  .title-month span { display: block; font-size: 44px; }
  .title-tagline {
    position: absolute; left: 230px; top: 44px; width: 300px; height: 96px; background: var(--sun);
    color: var(--navy); font-family: "Oswald", sans-serif; font-weight: 700; font-size: 36px;
    line-height: 1.05; padding: 10px 16px; text-transform: uppercase;
  }

  .impression {
    position: absolute; left: 650px; top: 168px; width: 176px; height: 176px; border-radius: 50%;
    background: var(--sun); border: 6px solid var(--navy); color: var(--navy); text-align: center;
    padding-top: 22px;
  }
  .impression .figure { font-family: "Oswald", sans-serif; font-weight: 700; font-size: 52px; line-height: 1; }
  .impression .note { font-size: 15px; line-height: 1.15; padding: 4px 16px 0; }

  .section-head {
    position: absolute; left: 113px; top: 416px; width: 623px; height: 44px; border: 3px solid var(--sun);
    color: var(--sun); font-family: "Oswald", sans-serif; font-size: 26px; text-align: center;
    line-height: 38px; letter-spacing: 1px;
  }

  .icon-slot { position: absolute; }
  .icon-work { left: 42px; top: 505px; width: 228px; height: 180px; }
  .icon-school { left: 380px; top: 485px; width: 130px; height: 205px; }
  .icon-people { left: 657px; top: 478px; width: 150px; height: 170px; }

  .stat { position: absolute; }
  .stat .figure { font-family: "Oswald", sans-serif; font-weight: 700; color: var(--sun); line-height: 1; white-space: nowrap; }
  .stat .label { font-size: 18px; text-transform: uppercase; letter-spacing: .3px; margin-top: 6px; white-space: nowrap; }
  .stat-work { left: 42px; top: 722px; }
  .stat-work .figure, .stat-school .figure { font-size: 66px; }
  .stat-school { left: 354px; top: 722px; }
  .stat-visits { left: 657px; top: 650px; width: 170px; }
  .stat-visits .figure { font-size: 84px; }
  .stat-visits .label { text-transform: none; font-size: 15px; line-height: 1.15; white-space: normal; margin-top: 2px; }

  .icon-reaction { left: 51px; top: 900px; width: 110px; height: 110px; border-radius: 50%; }
  .systemic {
    position: absolute; left: 184px; top: 896px; width: 360px; color: var(--sun);
    font-family: "Oswald", sans-serif; font-weight: 500; font-size: 28px; line-height: 1.12; text-transform: uppercase;
  }
  .preventable { position: absolute; left: 572px; top: 860px; width: 250px; height: 250px; }

  .footer {
    position: absolute; left: 0; bottom: 0; width: 100%; height: 80px; background: var(--navy);
    text-align: center; line-height: 80px; font-family: "Oswald", sans-serif; font-size: 28px; letter-spacing: 1px;
  }
</style>
</head>
<body>
<main class="poster">
  <header class="topline">A <span class="brand">PVR</span> INITIATIVE<span class="sep">|</span>AUGUST 2014 AS GUM CARE SEASON</header>

  <section class="title-block">
    <h1 class="title-month"><span>GUM CARE</span><span>SEASON</span></h1>
    <h2 class="title-tagline">Bright Grins for Every Year</h2>
  </section>

  <aside class="impression">
    <div class="figure">48%</div>
    <p class="note">remember a smile on first impression than anything else</p>
  </aside>

  <h3 class="section-head">WATCH YOUR MOUTH!</h3>

  <svg class="icon-slot icon-work" role="img" aria-label="Briefcase icon for lost work days" viewBox="0 0 228 180">
    <rect x="0" y="20" width="228" height="160" rx="10" fill="#17335b"/>
  </svg>
  <svg class="icon-slot icon-school" role="img" aria-label="Pencil icon for lost school days" viewBox="0 0 130 205">
    <rect x="0" y="0" width="130" height="205" rx="8" fill="#17335b"/>
  </svg>
  <svg class="icon-slot icon-people" role="img" aria-label="Icon of two young adults" viewBox="0 0 150 170">
    <rect x="0" y="0" width="150" height="170" rx="10" fill="#f8c227"/>
  </svg>

  <div class="stat stat-work">
    <div class="figure">1 MILLION</div>
    <div class="label">Lost days of work each year</div>
  </div>
  <div class="stat stat-school">
    <div class="figure">600,000</div>
    <div class="label">Days lost from school</div>
  </div>
  <div class="stat stat-visits">
    <div class="figure">50%</div>
    <div class="label">of 18–25 years old haven’t visited a dentist within past 12 months</div>
  </div>

  <svg class="icon-slot icon-reaction" role="img" aria-label="Surprised reaction icon" viewBox="0 0 110 110">
    <circle cx="55" cy="55" r="55" fill="#f8c227"/>
  </svg>
  <p class="systemic">More than 90 percent of all systemic diseases — including heart disease — have oral symptoms</p>

  <svg class="preventable" viewBox="0 0 250 250" aria-label="90% of all dental disease is preventable">
    <defs>
      <path id="ring-text" d="M 125 225 A 100 100 0 1 1 125.1 225"/>
    </defs>
    <circle cx="125" cy="125" r="62" fill="none" stroke="#17335b" stroke-width="26"/>
    <circle cx="125" cy="125" r="62" fill="none" stroke="#f8c227" stroke-width="26"
            stroke-dasharray="350.6 389.6" transform="rotate(-90 125 125)"/>
    <text x="125" y="136" text-anchor="middle" fill="#ffffff" font-family="Oswald, sans-serif" font-weight="700" font-size="32">90%</text>
    <text fill="#f8c227" font-family="Oswald, sans-serif" font-size="17" letter-spacing="1">
      <textPath href="#ring-text" startOffset="4%">OF ALL DENTAL DISEASE IS PREVENTABLE</textPath>
    </text>
  </svg>

  <footer class="footer">www.pivoradental.example</footer>
</main>
</body>
</html>
```